Signage setout with photos for side of Mowing Trailer

We need signage for our mowing trailer to attract new business.
Specifically a Rear sign 1470x880mm and Side signs 2400x880mm
Sign needs to be modern and professional.
Some example uploads as to what we have thought about so far.
Logo doesn't need to be the green colour.
Logo words and Logo of Mower do not need to be together.
Link to get a mower image>
https://brightfieldgear.example/tandem
Updates

Need extra days to review

Target Market(s)

Other Customers driving past the trailer.

Industry/Entity Type

Lawnmowing / Landscaping

Requirements
Must have
• Phone Number, Company Name & Logo, Web address, Chatterlane and Pixo Logos, Comment - "Acreage & Commercial Specialists" Catchcry - "100% Electric Mowing Company - est 2017" Services "Mowing, Hedging, Pressure Cleaning, Weed Control, Fencing, Turfing, Mulching and Rubbish Removal"
Nice to have
• Full colour background images.

```html
<!DOCTYPE html>
<html lang="en">
<head>
<meta charset="utf-8">
<title>Fresh Field Mowing – Trailer Signage Setout</title>
<link href="https://fonts.googleapis.com/css2?family=Barlow+Condensed:ital,wght@0,600;1,600;1,800;1,900&family=Poppins:ital,wght@0,700;1,800&family=Cabin:wght@500;600&family=Montserrat:ital,wght@0,400;0,700;1,700&display=swap" rel="stylesheet">
<style>
  :root{
    --bg-light:#d1d2d4;
    --bg-dark:#bcbdbf;
    --grass-mid:#4a9a34;
    --band-green:#1f6b32;
    --orange:#ee6a2a;
    --white:#ffffff;
    --ink:#1a1a1a;
    --mower:#6cc742;
  }
  *{margin:0;padding:0;box-sizing:border-box}
  html,body{width:1200px;height:933px;overflow:hidden}
  body{
    position:relative;
    background:linear-gradient(135deg,var(--bg-light) 0 62%,var(--bg-dark) 62% 100%);
    font-family:"Poppins",sans-serif;
  }
  .size-label{
    position:absolute;left:0;width:1200px;text-align:center;
    font-family:"Montserrat",sans-serif;font-weight:400;font-size:40px;color:var(--ink);
  }
  .size-label.top{top:42px}
  .size-label.bottom{top:836px}

  .sign{position:absolute;overflow:hidden;box-shadow:3px 4px 6px rgba(0,0,0,.35)}
  .sign.rear{left:320px;top:116px;width:560px;height:336px}
  .sign.side{left:142px;top:480px;width:916px;height:336px}

  .grass-photo{
    position:absolute;inset:0;
    background:
      linear-gradient(180deg,rgba(255,255,255,.08),rgba(0,0,0,0) 40%),
      repeating-linear-gradient(90deg,var(--grass-mid) 0 60px,#56a83a 60px 120px),
      var(--grass-mid);
  }
  .grass-photo::after{
    content:"";position:absolute;inset:0;
    background:radial-gradient(ellipse at 30% 20%,rgba(140,210,90,.35),transparent 60%),
               linear-gradient(180deg,transparent 60%,rgba(30,90,30,.35));
  }
  .mower-photo{
    position:absolute;border-radius:18px 18px 10px 10px;
    background:linear-gradient(180deg,#8c9a8c 0 14%,#3a4a3a 14% 20%,transparent 20% 34%,#2a2f2a 34% 48%,var(--mower) 48% 100%);
    opacity:.95;
  }
  .rear .mower-photo{left:12px;top:20px;width:228px;height:256px}
  .side .mower-photo{left:2px;top:22px;width:256px;height:286px}

  .brand{
    position:absolute;text-align:center;color:var(--white);
    font-family:"Cabin",sans-serif;font-weight:600;line-height:1;
    display:flex;flex-direction:column;align-items:center;gap:5px;
  }
  .brand .mark{width:34px;height:34px;border-radius:50%;background:var(--white)}
  .rear .brand{left:320px;top:20px;width:120px;font-size:16px}
  .side .brand{left:734px;top:22px;width:124px;font-size:19px}
  .brand .line2{font-size:1.3em}

  .headline{position:absolute;color:var(--white);text-align:center;text-shadow:1px 2px 3px rgba(0,0,0,.45);white-space:nowrap}
  .rear .headline{
    left:216px;top:108px;width:344px;font-family:"Poppins",sans-serif;
    font-weight:800;font-style:italic;font-size:25px;line-height:1.25;
  }
  .rear .headline .caps{font-size:27px}
  .side .headline{
    left:242px;top:134px;width:648px;font-family:"Barlow Condensed",sans-serif;
    font-weight:900;font-style:italic;font-size:52px;line-height:1;
  }

  .services{
    position:absolute;background:var(--orange);color:var(--white);
    font-family:"Barlow Condensed",sans-serif;font-weight:600;font-style:italic;
    text-align:center;line-height:1.25;
  }
  .rear .services{left:216px;top:176px;width:344px;height:38px;font-size:13px;padding-top:3px}
  .side .services{left:236px;top:198px;width:680px;height:30px;font-size:16.5px;line-height:30px;white-space:nowrap}

  .phone{position:absolute;display:flex;align-items:center;font-family:"Poppins",sans-serif;font-weight:800;font-style:italic;white-space:nowrap}
  .rear .phone{left:260px;top:216px;color:var(--white);font-size:38px;gap:8px;text-shadow:1px 2px 3px rgba(0,0,0,.4)}
  .rear .phone svg{width:36px;height:36px}
  .side .phone{left:282px;top:40px;color:var(--orange);font-size:66px;gap:12px;text-shadow:2px 2px 0 rgba(255,255,255,.7)}
  .side .phone svg{width:62px;height:62px}

  .catchcry{
    position:absolute;color:var(--orange);white-space:nowrap;
    font-weight:800;font-style:italic;
    text-shadow:1px 1px 0 #3b2412,0 0 2px rgba(0,0,0,.4);
  }
  .rear .catchcry{left:40px;top:278px;width:480px;text-align:center;font-family:"Poppins",sans-serif;font-size:20px}
  .side .catchcry{right:30px;top:240px;text-align:right;font-family:"Barlow Condensed",sans-serif;font-weight:900;font-size:37px;line-height:1.1}

  .web-band{position:absolute;background:var(--band-green)}
  .rear .web-band{left:0;top:308px;width:560px;height:28px}
  .side .web-band{left:306px;top:292px;width:610px;height:44px;border-top-left-radius:36px}
  .website{position:absolute;color:var(--white);font-family:"Montserrat",sans-serif;font-weight:700;font-style:italic;white-space:nowrap}
  .rear .website{left:106px;top:313px;font-size:14px;letter-spacing:3.3px}
  .side .website{left:456px;top:302px;font-size:19px;letter-spacing:3.8px}

  .socials{position:absolute;left:10px;top:310px;display:flex;gap:6px;
    font-family:"Cabin",sans-serif;font-size:8px;color:var(--white);align-items:center}
  .socials span{display:flex;align-items:center;gap:2px}
  .socials i{width:8px;height:8px;border-radius:50%;border:1.5px solid var(--white);display:inline-block}
</style>
</head>
<body>

<div class="size-label top">1470x880mm</div>

<section class="sign rear" aria-label="Rear sign 1470 by 880 mm">
  <div class="grass-photo" role="img" aria-label="Photo of a freshly mown striped lawn"></div>
  <div class="mower-photo" role="img" aria-label="Photo of a green electric zero-turn ride-on mower with solar canopy"></div>
  <div class="brand"><span class="mark"></span><span>FRESH FIELD</span><span class="line2">MOWING</span></div>
  <h2 class="headline">Acreage &amp; Commercial<br><span class="caps">SPECIALISTS</span></h2>
  <p class="services">• MOWING • HEDGING • PRESSURE CLEANING • WEED CONTROL<br>• FENCING • TURFING • MULCHING • RUBBISH REMOVAL</p>
  <div class="phone">
    <svg viewBox="0 0 40 40" aria-hidden="true"><circle cx="20" cy="20" r="19" fill="#fff"/><path d="M14 11c1-1 2-1 3 0l2 3c1 1 0 2-1 3l-1 1c1 3 3 5 6 6l1-1c1-1 2-2 3-1l3 2c1 1 1 2 0 3l-2 2c-6 1-15-8-14-14z" fill="none" stroke="#2f7a2a" stroke-width="2"/></svg>
    <span>3740-2916</span>
  </div>
  <p class="catchcry">100% Electric Mowing Company - est 2017</p>
  <div class="web-band"></div>
  <div class="socials"><span><i></i>Chatterlane</span><span><i></i>Pixo</span></div>
  <p class="website">www.freshfieldmowing.example</p>
</section>

<section class="sign side" aria-label="Side sign 2400 by 880 mm">
  <div class="grass-photo" role="img" aria-label="Photo of a freshly mown striped lawn"></div>
  <div class="mower-photo" role="img" aria-label="Photo of a green electric zero-turn ride-on mower with solar canopy"></div>
  <div class="phone">
    <svg viewBox="0 0 40 40" aria-hidden="true"><circle cx="20" cy="20" r="19" fill="#ee6a2a" stroke="#fff" stroke-width="1"/><path d="M14 11c1-1 2-1 3 0l2 3c1 1 0 2-1 3l-1 1c1 3 3 5 6 6l1-1c1-1 2-2 3-1l3 2c1 1 1 2 0 3l-2 2c-6 1-15-8-14-14z" fill="none" stroke="#fff" stroke-width="2"/></svg>
    <span>3740-2916</span>
  </div>
  <div class="brand"><span class="mark"></span><span>FRESH FIELD</span><span class="line2">MOWING</span></div>
  <h2 class="headline">Acreage &amp; Commercial Specialists</h2>
  <p class="services">• MOWING • HEDGING • PRESSURE CLEANING • WEED CONTROL • FENCING • TURFING • MULCHING • RUBBISH REMOVAL</p>
  <p class="catchcry">100% Electric Mowing Company - est 2017</p>
  <div class="web-band"></div>
  <p class="website">www.freshfieldmowing.example</p>
</section>

<div class="size-label bottom">2400x880mm</div>

</body>
</html>
```